Business card design for counselling and psychotherapy practice

I am seeking a business card for a new venture into private practice. I am based in Brisbane Qld Australia. I provide holistic counselling and psychotherapy to individuals and groups.
Some words that describe the underpinnings of this practice would include: being, becoming, awareness, wholeness, contact, safety, acceptance, relationship, gestalt, paradox, interconnected, nature, process.
I would like to see designs that include earth colours.
The overall design should communicate safety and a curiosity of being and becoming.
Target Market(s)
this design is marketed toward women, professionals, lesbian, transgender, mothers
Industry/Entity Type
Safety
Contact Information for Business Card
Willow & Tide
Counselling and Psychotherapy
Maren Olcott
ph: 0417382905
email: maren.willow&tide@quietmail.net
www.willow&tidecounselling&psychotherapy.net
Logo styles of interest
Abstract Logo
Look and feel
Each slider illustrates characteristics of the customer's brand and the style your logo design should communicate.

```html
<!DOCTYPE html>
<html lang="en">
<head>
<meta charset="utf-8">
<title>Willow &amp; Tide — Business Card</title>
<link rel="stylesheet" href="https://fonts.googleapis.com/css2?family=Arimo:wght@700&family=Open+Sans:wght@400;700&family=Sorts+Mill+Goudy&display=swap">
<style>
  :root {
    --page-bg: #ffffff;
    --blue-deep: #073f8a;
    --blue-main: #0a4f9f;
    --blue-light: #1f6fbd;
    --blue-band: #2170ba;
    --band-white: #ffffff;
    --card-edge: #1a1a1a;
    --text-light: #ffffff;
    --text-contact: #4a4a4a;
  }
  html, body {
    margin: 0;
    padding: 0;
    width: 1200px;
    height: 728px;
    overflow: hidden;
    background: var(--page-bg);
  }
  .canvas {
    position: relative;
    width: 1200px;
    height: 728px;
  }
  .card-shape {
    position: absolute;
    left: 0;
    top: 0;
  }
  .practice-name {
    position: absolute;
    left: 278px;
    top: 276px;
    margin: 0;
    font-family: "Arimo", Arial, sans-serif;
    font-weight: 700;
    font-size: 35px;
    line-height: 46px;
    color: var(--text-light);
    letter-spacing: 0.2px;
  }
  .practitioner {
    position: absolute;
    left: 765px;
    top: 174px;
    font-family: "Open Sans", Arial, sans-serif;
    color: var(--text-light);
  }
  .practitioner-name {
    display: block;
    font-weight: 700;
    font-size: 18px;
    line-height: 24px;
  }
  .practitioner-phone {
    display: block;
    font-weight: 400;
    font-size: 16.5px;
    line-height: 24px;
  }
  .contact-lines {
    position: absolute;
    left: 278px;
    top: 436px;
    font-family: "Sorts Mill Goudy", Georgia, serif;
    font-size: 21px;
    line-height: 29px;
    color: var(--text-contact);
    white-space: nowrap;
  }
  .contact-lines span { display: block; }
</style>
</head>
<body>
<main class="canvas">
  <svg class="card-shape" width="1200" height="728" viewBox="0 0 1200 728" aria-hidden="true">
    <defs>
      <clipPath id="card-clip">
        <path d="M365,145 H943 V500 A58,58 0 0 1 885,558 H219 V290 A145,145 0 0 1 365,145 Z"/>
      </clipPath>
      <linearGradient id="top-panel-fill" x1="0" y1="0" x2="1" y2="1">
        <stop offset="0" stop-color="var(--blue-main)"/>
        <stop offset="1" stop-color="var(--blue-main)"/>
      </linearGradient>
    </defs>
    <g clip-path="url(#card-clip)">
      <rect class="top-panel" x="219" y="145" width="724" height="282" fill="var(--blue-main)"/>
      <polygon class="sweep-dark" points="219,145 405,145 600,427 219,427" fill="var(--blue-deep)" opacity="0.55"/>
      <polygon class="sweep-light" points="520,300 943,210 943,427 640,427" fill="var(--blue-light)" opacity="0.45"/>
      <path class="sweep-curve" d="M430,250 Q680,330 943,430 L943,427 L430,427 Z" fill="var(--blue-light)" opacity="0.25"/>
      <rect class="contact-band" x="219" y="427" width="724" height="79" fill="var(--band-white)"/>
      <rect class="base-band" x="219" y="506" width="724" height="52" fill="var(--blue-band)"/>
      <polygon class="base-sweep" points="690,506 943,506 943,558 730,558" fill="#2a7cc6" opacity="0.6"/>
    </g>
    <path d="M365,145 H943 V500 A58,58 0 0 1 885,558 H219 V290 A145,145 0 0 1 365,145 Z" fill="none" stroke="var(--card-edge)" stroke-width="1.2"/>
  </svg>

  <div class="practitioner">
    <span class="practitioner-name">Maren Olcott</span>
    <span class="practitioner-phone">Ph : 041-738-2905</span>
  </div>

  <h1 class="practice-name">Willow &amp; Tide<br>Counselling and Psychotherapy</h1>

  <div class="contact-lines">
    <span class="contact-email">E-mail : maren.willow&amp;tide@quietmail.net</span>
    <span class="contact-web">Web : &nbsp;www.willow&amp;tidecounselling&amp;psychotherapy.net</span>
  </div>
</main>
</body>
</html>
```